Business card design

Hi,
I need to have a business card design based on the current logo.
If competitive I not put it out to everyone.

It can be single of double sided

Target Market(s)

Food businesses

Industry/Entity Type

Food Manufacturing

Contact Information for Business Card

Details will on card will be as follows Name = Marcus Pell Email = Marcus@BrimKitchens.com.au Phone = 0418562307 Address = 57 Tallowmere Road , Fortitude Valley QLD 4006 Australia

Font styles to use
Other font styles liked:
• based on two fonts - Adelle & Museo

Requirements
Must have
• Based on the on switch concept

```html
<!DOCTYPE html>
<html lang="en">
<head>
<meta charset="utf-8">
<title>BrimKitchens Business Card</title>
<link rel="stylesheet" href="https://fonts.googleapis.com/css2?family=Arimo:wght@400;700&display=swap">
<style>
  :root {
    --backdrop: #b4b4b4;
    --brand-red: #ec2648;
    --brand-brown: #3e2729;
    --card-white: #ffffff;
    --text-dark: #2b2325;
    --rule-grey: #8a8a8a;
  }
  * { box-sizing: border-box; margin: 0; padding: 0; }
  html, body {
    width: 1200px;
    height: 1200px;
    overflow: hidden;
    background: var(--backdrop);
    font-family: "Arimo", Arial, sans-serif;
  }
  .stage {
    position: relative;
    width: 1200px;
    height: 1200px;
  }
  .card {
    position: absolute;
    top: 303px;
    height: 594px;
  }
  .card-back {
    left: 201px;
    width: 369px;
    background: var(--brand-brown);
    display: flex;
    flex-direction: column;
    align-items: center;
    justify-content: center;
    gap: 34px;
  }
  .back-dot {
    width: 190px;
    height: 190px;
    border-radius: 50%;
    background: var(--brand-red);
  }
  .back-name {
    color: var(--brand-red);
    font-weight: 700;
    font-size: 30px;
    letter-spacing: 1px;
  }
  .card-front {
    left: 599px;
    width: 364px;
    background: var(--card-white);
    color: var(--text-dark);
    text-align: center;
  }
  .wordmark {
    position: absolute;
    top: 134px;
    left: 0;
    right: 0;
    display: flex;
    align-items: center;
    justify-content: center;
    gap: 10px;
  }
  .wordmark-dot {
    width: 34px;
    height: 34px;
    border-radius: 50%;
    background: var(--brand-red);
  }
  .wordmark-name {
    color: var(--brand-brown);
    font-weight: 700;
    font-size: 28px;
    letter-spacing: 0.5px;
  }
  .person-name {
    position: absolute;
    top: 334px;
    left: 0;
    right: 0;
    color: var(--brand-red);
    font-weight: 700;
    font-size: 22px;
    letter-spacing: 0.5px;
  }
  .icon-row {
    position: absolute;
    top: 374px;
    left: 87px;
    width: 190px;
    display: flex;
    align-items: center;
    gap: 4px;
  }
  .icon-row .rule {
    flex: 1;
    height: 1px;
    background: var(--rule-grey);
  }
  .icon-tile {
    width: 25px;
    height: 25px;
    border-radius: 3px;
    background: var(--brand-red);
    display: flex;
    align-items: center;
    justify-content: center;
  }
  .contact-lines {
    position: absolute;
    top: 408px;
    left: 0;
    right: 0;
    font-size: 16px;
    line-height: 21.5px;
  }
  .contact-lines .accent { color: var(--brand-red); }
  .divider {
    position: absolute;
    top: 478px;
    left: 88px;
    width: 195px;
    height: 1px;
    background: var(--rule-grey);
  }
  .address {
    position: absolute;
    top: 488px;
    left: 0;
    right: 0;
    font-size: 16px;
    line-height: 21.5px;
    font-style: normal;
  }
</style>
</head>
<body>
<main class="stage">
  <section class="card card-back" aria-label="Card back">
    <div class="back-dot"></div>
    <div class="back-name">BRIMKITCHENS</div>
  </section>

  <section class="card card-front" aria-label="Card front">
    <div class="wordmark">
      <span class="wordmark-dot"></span>
      <span class="wordmark-name">BRIMKITCHENS</span>
    </div>

    <h1 class="person-name">MARCUS PELL</h1>

    <div class="icon-row">
      <span class="rule"></span>
      <span class="icon-tile" aria-label="Phone">
        <svg width="15" height="15" viewBox="0 0 16 16" fill="#fff"><path d="M1 6c0-2 3-3 7-3s7 1 7 3v1h-3V5.5H4V7H1z"/><rect x="3" y="8" width="10" height="6" rx="1"/></svg>
      </span>
      <span class="icon-tile" aria-label="Email">
        <svg width="16" height="12" viewBox="0 0 16 12" fill="none" stroke="#fff" stroke-width="1.2"><rect x="1" y="1" width="14" height="10"/><path d="M1 1l7 6 7-6M1 11l5-5M15 11l-5-5"/></svg>
      </span>
      <span class="icon-tile" aria-label="Website">
        <svg width="15" height="15" viewBox="0 0 16 16"><circle cx="8" cy="8" r="6.5" fill="#fff"/><path d="M5 4c2 0 3 2 2 3s-2 1-1 3-1 2-2 1M10 9c1-1 3 0 2 2" stroke="var(--brand-red)" stroke-width="1.5" fill="none"/></svg>
      </span>
      <span class="rule"></span>
    </div>

    <div class="contact-lines">
      <div>0418562307</div>
      <div>Marcus@BrimKitchens.com.au</div>
      <div>www.<span class="accent">BrimKitchens</span>.com.au</div>
    </div>

    <div class="divider"></div>

    <address class="address">
      <div>57 Tallowmere Road</div>
      <div>Quillan Heights</div>
      <div>NSW 2874 Australia</div>
    </address>
  </section>
</main>
</body>
</html>
```